Township of Quenford E-Alert Signup

Need to create print media that is designed for a Town in New Jersey that is starting a marketing campaign to get townspeople to sign up for the E-Alert system.Need print media that is 1. interchangeable in size (regular letter-size, as well as a poster size) 2. Branded with their colors, logo, etc. (green and white displayed in logo)3. Displays the incentives to sign up. Incentives:- Community Services/Announcements- Gov’t/Non-profit Resources- Tax Information- Employment opportunities- Municipal Services/Public Works/Recreation Divisions- Health Updates
Target Market(s)
Townspeople of Maplewood NJ
Industry/Entity Type
Government
Colors
Designer to choose colors to be used in the design.
Requirements
Must have
- 1. interchangeable in size (regular letter-size, as well as a poster size)
- 2. Branded with their colors, logo, etc. (green and white displayed in logo)
- 3. Displays the incentives to sign up.
- Incentives:
- - Community Services/Announcements
- - Gov’t/Non-profit Resources
- - Tax Information
- - Employment opportunities
- - Municipal Services/Public Works/Recreation Divisions
- - Health Updates

```html
<!DOCTYPE html>
<html lang="en">
<head>
<meta charset="utf-8">
<title>Township of Quenford – E-Alert Signup</title>
<link href="https://fonts.googleapis.com/css2?family=Arimo:ital,wght@0,700;1,700&family=Tinos:wght@700&display=swap" rel="stylesheet">
<style>
  :root{
    --green-dark:#1f7a1f;
    --green-mid:#4a9a2a;
    --green-lime:#a8c92a;
    --green-seal:#2a8a35;
    --grey-soft:#d8d8d8;
    --ink:#222222;
    --white:#ffffff;
  }
  html,body{margin:0;padding:0;overflow:hidden;background:var(--white);}
  .flyer{position:relative;width:928px;height:1200px;overflow:hidden;font-family:"Arimo",Arial,sans-serif;}
  .flyer-art{position:absolute;inset:0;}
  .town-name{position:absolute;left:238px;top:252px;margin:0;font-family:"Tinos","Times New Roman",serif;font-weight:700;color:var(--green-seal);line-height:1;}
  .town-name .town{display:block;font-size:37px;letter-spacing:0.5px;}
  .town-name .state{display:block;font-size:27px;margin-top:8px;padding-left:28px;}
  .headline{position:absolute;left:0;top:0;margin:0;font-style:italic;font-weight:700;}
  .headline .lead{position:absolute;left:431px;top:362px;font-size:39px;color:var(--green-dark);white-space:nowrap;}
  .headline .big{position:absolute;font-size:124px;color:var(--ink);letter-spacing:-3px;white-space:nowrap;line-height:1;}
  .headline .e-alert{left:370px;top:404px;}
  .headline .system{left:438px;top:508px;}
  .benefits{position:absolute;right:18px;top:632px;margin:0;padding:0;list-style:none;text-align:right;font-style:italic;font-weight:700;font-size:28px;line-height:34.4px;color:var(--ink);}
  .footer{position:absolute;right:20px;top:1128px;text-align:right;font-style:italic;font-weight:700;font-size:17px;line-height:20px;color:var(--white);}
  .footer p{margin:0;}
</style>
</head>
<body>
<main class="flyer">
  <svg class="flyer-art" width="928" height="1200" viewBox="0 0 928 1200">
    <defs>
      <linearGradient id="topPhoto" x1="0" y1="0" x2="1" y2="1">
        <stop offset="0" stop-color="#3f6fc0"/>
        <stop offset="0.45" stop-color="#8a7f70"/>
        <stop offset="1" stop-color="#5e5346"/>
      </linearGradient>
      <linearGradient id="bottomPhoto" x1="0" y1="0" x2="0" y2="1">
        <stop offset="0" stop-color="#aac4dc"/>
        <stop offset="0.45" stop-color="#c9d4dc"/>
        <stop offset="0.75" stop-color="#6a7a4a"/>
        <stop offset="1" stop-color="#3e5a2a"/>
      </linearGradient>
      <linearGradient id="ovalPhoto" x1="0" y1="0" x2="1" y2="1">
        <stop offset="0" stop-color="#6f9a4f"/>
        <stop offset="0.5" stop-color="#5a5c60"/>
        <stop offset="1" stop-color="#7aa060"/>
      </linearGradient>
      <linearGradient id="darkBand" x1="0" y1="0" x2="1" y2="0">
        <stop offset="0" stop-color="#1c6d14"/>
        <stop offset="0.6" stop-color="#2f8a1e"/>
        <stop offset="1" stop-color="#1c6d14"/>
      </linearGradient>
      <linearGradient id="limeBand" x1="0" y1="0" x2="1" y2="0">
        <stop offset="0" stop-color="#a9c92a"/>
        <stop offset="0.7" stop-color="#c8dc6a"/>
        <stop offset="1" stop-color="#9cc12a"/>
      </linearGradient>
      <linearGradient id="panelFade" x1="0" y1="0" x2="1" y2="0">
        <stop offset="0" stop-color="#ffffff" stop-opacity="0.25"/>
        <stop offset="1" stop-color="#ffffff" stop-opacity="0.6"/>
      </linearGradient>
    </defs>

    <rect class="photo-top" x="0" y="0" width="928" height="520" fill="url(#topPhoto)" role="img" aria-label="Photo of historic brick storefront buildings in the town center under a blue sky"/>
    <rect class="photo-bottom" x="0" y="470" width="928" height="730" fill="url(#bottomPhoto)" role="img" aria-label="Photo of the town hall with its white cupola, a flagpole and green trees"/>

    <path class="wave-white" d="M0,225 C150,170 330,160 480,210 C600,250 720,300 928,330 L928,380 C700,520 300,560 0,500 Z" fill="var(--white)"/>
    <rect class="benefits-panel" x="565" y="600" width="363" height="460" fill="url(#panelFade)"/>
    <path class="band-dark" d="M40,496 C330,560 700,520 928,368 L928,415 C760,540 420,615 46,604 Z" fill="url(#darkBand)"/>
    <path class="band-lime" d="M92,615 C400,640 700,560 928,420 L928,500 C720,640 420,720 100,727 Z" fill="url(#limeBand)"/>

    <ellipse class="oval-frame" cx="765" cy="281" rx="152" ry="98" fill="var(--white)"/>
    <ellipse class="oval-photo" cx="765" cy="281" rx="142" ry="88" fill="url(#ovalPhoto)" role="img" aria-label="Aerial photo of a street intersection painted with a rainbow crosswalk"/>

    <circle class="seal-ring" cx="131" cy="354" r="120" fill="var(--white)" stroke="var(--green-seal)" stroke-width="4"/>
    <text class="seal-name" x="131" y="346" text-anchor="middle" font-family="Tinos, 'Times New Roman', serif" font-weight="700" font-size="21" fill="var(--green-seal)">
      <tspan x="131">Township of</tspan>
      <tspan x="131" dy="26">Quenford</tspan>
    </text>

    <path class="footer-white" d="M0,1200 L0,1150 L928,1032 L928,1200 Z" fill="var(--white)"/>
    <path class="footer-lime" d="M0,1200 L928,1062 L928,1082 L120,1200 Z" fill="var(--green-lime)"/>
    <path class="footer-green" d="M60,1200 L928,1078 L928,1200 Z" fill="var(--green-dark)"/>

    <g class="footer-badge" transform="translate(792 1094)">
      <circle r="24" fill="var(--white)" stroke="var(--green-dark)" stroke-width="3"/>
      <path d="M-9,-11 L-4,-12 L-1,-4 L-5,-1 C-3,4 1,7 5,9 L8,5 L14,8 L13,13 C3,14 -12,1 -9,-11 Z" fill="var(--green-dark)"/>
    </g>

    <g class="service-icons" aria-label="Service icons: announcements, town hall, forms, exchange, meetings, settings, messages, health">
      <g class="icon-announce" transform="translate(128 1118)">
        <path d="M-22,-6 L6,-22 L6,22 L-22,6 Z" fill="var(--green-dark)"/>
        <rect x="-30" y="-8" width="10" height="16" fill="var(--green-dark)"/>
        <path d="M14,-12 Q22,0 14,12 M20,-18 Q32,0 20,18" fill="none" stroke="var(--green-dark)" stroke-width="3" stroke-linecap="round"/>
      </g>

      <g class="icon-townhall" transform="translate(192 1123)">
        <circle r="38" fill="var(--green-mid)" stroke="var(--white)" stroke-width="4"/>
        <path d="M-20,-2 L0,-18 L20,-2 Z" fill="var(--white)"/>
        <rect x="-16" y="-2" width="32" height="20" fill="var(--white)"/>
        <rect x="-4" y="6" width="8" height="12" fill="var(--green-mid)"/>
        <rect x="-12" y="3" width="5" height="5" fill="var(--green-mid)"/>
        <rect x="7" y="3" width="5" height="5" fill="var(--green-mid)"/>
      </g>

      <g class="icon-forms" transform="translate(258 1108)">
        <circle r="35" fill="var(--green-lime)" stroke="var(--white)" stroke-width="4"/>
        <rect x="-13" y="-17" width="26" height="34" rx="2" fill="var(--white)"/>
        <path d="M-8,-9 H8 M-8,-2 H8 M-8,5 H8 M-8,12 H2" stroke="var(--green-mid)" stroke-width="2.5"/>
      </g>

      <g class="icon-exchange" transform="translate(331 1104)">
        <circle r="35" fill="var(--grey-soft)" stroke="var(--white)" stroke-width="4"/>
        <path d="M-16,-7 H14 M8,-13 L14,-7 L8,-1 M16,7 H-14 M-8,1 L-14,7 L-8,13" fill="none" stroke="var(--green-dark)" stroke-width="3.5" stroke-linecap="round" stroke-linejoin="round"/>
      </g>

      <g class="icon-meetings" transform="translate(400 1085)">
        <circle r="38" fill="var(--white)" stroke="var(--green-mid)" stroke-width="4"/>
        <rect x="-18" y="-15" width="36" height="24" rx="2" fill="var(--green-mid)"/>
        <path d="M-8,-3 L-2,3 L9,-8" fill="none" stroke="var(--white)" stroke-width="3.5" stroke-linecap="round" stroke-linejoin="round"/>
        <path d="M-12,9 L-16,19 M12,9 L16,19" stroke="var(--green-mid)" stroke-width="3" stroke-linecap="round"/>
      </g>

      <g class="icon-settings" transform="translate(469 1073)">
        <circle r="35" fill="var(--white)" stroke="var(--green-dark)" stroke-width="6"/>
        <circle r="15" fill="none" stroke="var(--green-mid)" stroke-width="7" stroke-dasharray="5.9 5.9"/>
        <circle r="10" fill="var(--green-mid)"/>
        <circle r="4.5" fill="var(--white)"/>
      </g>

      <g class="icon-messages" transform="translate(542 1062)">
        <circle r="35" fill="var(--green-lime)" stroke="var(--white)" stroke-width="4"/>
        <path d="M-18,-14 H18 V8 H-4 L-12,16 V8 H-18 Z" fill="var(--white)" stroke-linejoin="round"/>
        <path d="M-10,-5 H10 M-10,1 H4" stroke="var(--green-lime)" stroke-width="2.5"/>
      </g>

      <g class="icon-health" transform="translate(611 1050)">
        <circle r="35" fill="var(--white)" stroke="var(--green-mid)" stroke-width="5"/>
        <path d="M-6,-18 H6 V-6 H18 V6 H6 V18 H-6 V6 H-18 V-6 H-6 Z" fill="var(--green-mid)"/>
      </g>
    </g>
  </svg>

  <h2 class="town-name"><span class="town">QUENFORD</span><span class="state">NEW JERSEY</span></h2>

  <h1 class="headline">
    <span class="lead">Sign up in the</span>
    <span class="big e-alert">E-Alert</span>
    <span class="big system">System</span>
  </h1>

  <ul class="benefits">
    <li>get access to:</li>
    <li>- Community Services</li>
    <li>- Announcements</li>
    <li>- Gov't/Non-profit</li>
    <li>Resources</li>
    <li>- Tax Information</li>
    <li>- Employment</li>
    <li>opportunities</li>
    <li>- Municipal Services /</li>
    <li>Public Works/</li>
    <li>Recreation Divisions</li>
    <li>- Health Updates</li>
  </ul>

  <footer class="footer">
    <p>Quenford New Jersey</p>
    <p>218 Orchard Ave., Quenford Township, NJ 07192</p>
    <p>Hours of Operation 9:00 am - 4:30 pm | Ph: (973) 555-0147</p>
  </footer>
</main>
</body>
</html>
```